Redesign of existing Web Design Project

I wish to redsesign the web pages on www.qbrl.com.au

Background of Harlowe Bexley

Harlowe Bexley Construction Services was established in 2004 as a boutique construction company offering construction advice and management services. We assist people in the construction minefield – step by step.

We offer services in: -

• Construction Management
• Project Management
• Building

The essence of our business is ensuring every project we undertake achieves the client’s objectives. Our experience has shown the secrets to a profitable project are -

• Planning
• Attention to detail
• Value add

We take the trouble to understand the client’s needs in person. Our hands-on approach ensures those involved deliver to the required quality standards at the scheduled times.

Our area of works include: -

• Residential single and multistorey developments
• Education facilities
• Suburban commercial building and refurbishment
• Health
• Defence
• Industrial

Objective of Acquisition

We are planning to expand our business activities. We are aiming to increase our turnover and use website as an increased passive selling tool.

Possible company type

This is an ideal opportunity for person who can capture readers attention.

Target Market(s)

see www.qbrl.com.au

Industry/Entity Type

Construction

Requirements
Must have
• Capture peoples attention on readers zones

```html
<!DOCTYPE html>
<html lang="en">
<head>
<meta charset="utf-8">
<title>Harlowe Bexley Construction Services</title>
<link href="https://fonts.googleapis.com/css2?family=Ubuntu:wght@400;500&family=Open+Sans:wght@400&family=Gelasio&display=swap" rel="stylesheet">
<style>
:root{
  --header:#23282c;
  --teal:#2b8e9b;
  --teal-dark:#15535f;
  --beige:#d7cfb4;
  --page:#f3f3f3;
  --footer:#3d4c55;
  --text:#2a2a2a;
  --rust:#7a3113;
  --slate:#3e4a52;
  --quote:#1e6f86;
}
*{margin:0;padding:0;box-sizing:border-box}
html,body{width:1200px;height:1200px;overflow:hidden}
body{position:relative;background:#fff;font-family:"Open Sans",sans-serif;color:var(--text)}
.abs{position:absolute}
.site-header{left:0;top:0;width:1200px;height:95px;background:var(--header)}
.brand{left:140px;top:38px;display:flex;align-items:center;gap:12px;font-family:"Ubuntu",sans-serif;font-size:26px;color:#e8eef3}
.brand-mark{width:30px;height:30px;background:#8da6d8}
.top-tab{left:735px;top:0;width:345px;height:35px;background:var(--teal);border-radius:0 0 30px 30px;font-family:"Ubuntu",sans-serif;color:#fff;display:flex;align-items:center}
.top-tab .contact{margin-left:16px;font-size:14px}
.top-tab .follow{margin-left:60px;font-size:11px}
.social{width:20px;height:20px;margin-left:6px;border-radius:3px}
.jump-field{left:767px;top:53px;width:210px;height:24px;background:#fff;border-radius:12px;font-size:10px;color:#555;display:flex;align-items:center}
.jump-field span{margin-left:12px}
.jump-field .sel{margin-left:36px;padding-left:6px;border-left:1px dotted #999;font-size:11px;flex:1}
.jump-field svg{margin-right:6px}
.jump-btn{left:981px;top:53px;width:63px;height:24px;background:var(--teal);border-radius:0 12px 12px 0;color:#fff;font:500 13px "Ubuntu",sans-serif;text-align:center;line-height:24px}
.hero-band{left:0;top:95px;width:1200px;height:386px;background:var(--beige)}
.hero{left:115px;top:108px;width:774px;height:355px;background:linear-gradient(160deg,#5d8a8d,#9bb4ad 45%,#5a5c4a)}
.thumb{left:901px;width:181px}
.thumb.t1{top:108px;height:113px;background:linear-gradient(160deg,#6f9597,#3f4a3c)}
.thumb.t2{top:231px;height:107px;background:linear-gradient(160deg,#ecd4c4,#d9b9a6)}
.thumb.t3{top:348px;height:113px;background:linear-gradient(160deg,#dfe2e8,#c9ccd4)}
.nav-band{left:0;top:481px;width:1200px;height:52px;background:var(--teal-dark)}
.main-nav{left:99px;top:463px;width:1002px;height:60px;background:var(--teal);font-family:"Ubuntu",sans-serif;font-size:14.5px;color:#fff;display:flex;align-items:center;padding-left:11px;white-space:nowrap}
.main-nav span.sep{margin:0 15px}
.nav-pointer{left:122px;top:523px}
.page{left:109px;top:533px;width:982px;height:553px;background:var(--page)}
.divider{top:548px;width:4px;height:506px;background:linear-gradient(90deg,#ccc,#e9e9e9)}
h1.welcome{left:124px;top:550px;font:400 19px "Ubuntu",sans-serif;color:var(--rust)}
h1.welcome b{font-weight:400;color:#333}
.intro{left:124px;top:590px;width:380px;font-size:12.5px;line-height:15.8px;text-align:justify}
.philosophy{left:141px;top:667px;width:339px;height:48px;background:linear-gradient(90deg,#c9ada0,#ece3df);box-shadow:3px 3px 4px #bbb;font-family:"Gelasio",serif;padding:5px 7px;overflow:hidden;white-space:nowrap}
.philosophy small{font-size:12.5px;line-height:16px;color:#6d3b24;display:block}
.philosophy p{font-size:13.5px;line-height:20px;letter-spacing:-0.2px;color:#111}
h2.who{left:124px;top:726px;font:400 15px "Ubuntu",sans-serif;color:var(--rust)}
.users{left:131px;top:755px;width:373px;list-style:none;font-size:12.5px;line-height:16px}
.users li{padding-left:15px;position:relative;margin-bottom:8px;text-align:justify}
.users li::before{content:"";position:absolute;left:0;top:3px;width:7px;height:7px;border:1px solid #6ea0c8}
.closing{left:124px;top:1021px;font-size:12.5px}
.read-more{left:435px;top:1048px;width:71px;height:20px;background:var(--teal);border-radius:6px 6px 0 0;color:#fff;font-size:11px;text-align:center;line-height:22px}
.brush{display:flex;align-items:center;justify-content:center;color:#fff;font:400 17px "Ubuntu",sans-serif;border-radius:50%}
.brush.testi{left:552px;top:550px;width:160px;height:48px;background:radial-gradient(ellipse,#5a3222 55%,rgba(90,50,34,0) 72%)}
.brush.gallery{left:546px;top:812px;width:150px;height:52px;background:radial-gradient(ellipse,#1c4f7d 55%,rgba(28,79,125,0) 72%)}
.testimonial{left:564px;top:618px;width:250px;font-size:12.5px;line-height:15.8px}
.testimonial .body{text-align:justify}
.testimonial .quote{margin-top:15px;color:var(--quote);font-style:italic;text-align:justify}
.testimonial .by{margin-top:2px}
.gal{width:100px;height:66px}
.g1{left:575px;top:884px;background:linear-gradient(90deg,#eee,#b77b45)}
.g2{left:699px;top:884px;background:linear-gradient(160deg,#b08a68,#6b7f8f)}
.g3{left:575px;top:968px;background:linear-gradient(160deg,#d6c7b4,#8c5b36)}
.g4{left:699px;top:968px;background:linear-gradient(160deg,#d4d8da,#8d6f57)}
.services{left:857px;top:558px;width:244px;height:141px;background:#5a6a73;padding:6px 0 0 6px}
.services div{height:38px;background:var(--slate);margin-bottom:6px;display:flex;align-items:center;color:#fff;font:400 14.5px "Ubuntu",sans-serif;letter-spacing:.3px;white-space:nowrap}
.services svg{margin:0 10px 0 12px}
.promo-gallery{left:855px;top:736px;width:227px;height:71px;background:linear-gradient(90deg,#c2561d,#8a3c10);box-shadow:2px 3px 4px #999;color:#fff;font:500 17px/15px "Ubuntu",sans-serif;padding:19px 9px}
.promo-gallery small{display:block;font-size:14px}
.promo-gallery em{display:block;font:400 9px "Ubuntu",sans-serif;margin-top:6px;font-style:normal}
.promo-gallery .crew{position:absolute;right:0;top:0;width:95px;height:71px;background:linear-gradient(160deg,#d9cf6a,#6a7f8f)}
.brochure{left:857px;top:839px;width:223px;height:58px;background:#1c1e20;color:#fff;font:400 15px "Ubuntu",sans-serif;display:flex;align-items:center;padding-left:10px;gap:8px;white-space:nowrap}
.brochure .doc{width:34px;height:40px;background:linear-gradient(#e8eef5,#8fa7c8)}
.other{left:886px;top:963px;font:400 20px/19px "Ubuntu",sans-serif;color:#111;letter-spacing:.5px}
.site-footer{left:0;top:1086px;width:1200px;height:114px;background:var(--footer);color:#d9e0e4;font-size:11.5px;text-align:center}
.site-footer p{position:absolute;width:100%;white-space:nowrap}
</style>
</head>
<body>
<header class="site-header abs"></header>
<div class="brand abs"><span class="brand-mark"></span>Harlowe Bexley Construction Services</div>
<div class="top-tab abs"><span class="contact">Contact Us</span><span class="follow">Follow Us on :</span><span class="social" style="background:#2b6fb3"></span><span class="social" style="background:#27a7dd"></span><span class="social" style="background:#3b5b9c"></span></div>
<div class="jump-field abs"><span>Quick jump to</span><span class="sel">Home</span><svg width="14" height="10"><path d="M0 0h14L7 10z" fill="#777"/></svg></div>
<div class="jump-btn abs">Jump</div>

<div class="hero-band abs"></div>
<div class="hero abs" role="img" aria-label="Site engineer in a hard hat holding rolled plans, building site behind"></div>
<div class="thumb t1 abs" role="img" aria-label="Engineer with plans"></div>
<div class="thumb t2 abs" role="img" aria-label="Hand drafting with a pencil"></div>
<div class="thumb t3 abs" role="img" aria-label="Blueprints and drafting tools"></div>

<div class="nav-band abs"></div>
<nav class="main-nav abs">Home<span class="sep">|</span>About Us<span class="sep">|</span>Building<span class="sep">|</span>Construction Management<span class="sep">|</span>Project Management<span class="sep">|</span>Links<span class="sep">|</span>Free Downloads<span class="sep">|</span>Careers<span class="sep">|</span>Contacts</nav>
<svg class="nav-pointer abs" width="24" height="14"><path d="M0 0h24L12 14z" fill="#2b8e9b"/></svg>

<main class="page abs"></main>
<div class="divider abs" style="left:533px"></div>
<div class="divider abs" style="left:841px"></div>

<h1 class="welcome abs">Welcome to <b>Harlowe Bexley</b></h1>
<p class="intro abs">We are a Sydney based Construction Company who can help with all your construction needs. The Harlowe Bexley process helps define your budget, establishes Return on Investment and reduces potential risk.</p>
<div class="philosophy abs"><small>Our philosophy is simple:</small><p>"Deliver the project you want on time, to budget."</p></div>
<h2 class="who abs">Who uses us?</h2>
<ul class="users abs">
<li>Architects – to assist with costing a project, value-engineering and project implementation.</li>
<li>Owner/Builders – to assist with project management, costings, work flow and final sign offs</li>
<li>Developers – to assist with costings, tender appraisal and project management</li>
<li>Strata managers – remediation, fire safety</li>
<li>Sub-contractors – for pricing assistance</li>
<li>Lessor and lessees – for fit outs and make good work</li>
<li>Investors – to define profitability, feasibility and risk</li>
<li>Finance companies – risk analysis</li>
<li>Solicitors – advisory services</li>
</ul>
<p class="closing abs">Construction is a minefield. We’ll help you through it!</p>
<div class="read-more abs">read more</div>

<div class="brush testi abs">Testimonials</div>
<div class="testimonial abs">
<p class="body">Harlowe Bexley is a construction company with significant skills in Project and Construction Management. We will help you undertake a successful construction.</p>
<p class="quote">“The success of our Newcastle project built our confidence in the ability of Harlowe Bexley.”</p>
<p class="by">Martin Keane Director Ardent Builders</p>
</div>
<div class="brush gallery abs">Gallery</div>
<div class="gal g1 abs" role="img" aria-label="Interior with pendant light and timber wall"></div>
<div class="gal g2 abs" role="img" aria-label="Living area with staircase"></div>
<div class="gal g3 abs" role="img" aria-label="Kitchen and dining room"></div>
<div class="gal g4 abs" role="img" aria-label="Glass balustrade staircase"></div>

<div class="services abs">
<div><svg width="20" height="18"><path d="M2 10l5 6L18 2" stroke="#7cc62d" stroke-width="4" fill="none"/></svg>Project Management</div>
<div><svg width="20" height="18"><path d="M2 10l5 6L18 2" stroke="#7cc62d" stroke-width="4" fill="none"/></svg>Construction Management</div>
<div><svg width="20" height="18"><path d="M2 10l5 6L18 2" stroke="#7cc62d" stroke-width="4" fill="none"/></svg>Building</div>
</div>
<div class="promo-gallery abs">PROJECT<small>GALLERY PICS</small><em>⇨ click here</em><span class="crew" role="img" aria-label="Two builders in hard hats reviewing plans"></span></div>
<div class="brochure abs"><span class="doc" role="img" aria-label="Brochure cover"></span>Information Brochure</div>
<p class="other abs">Some Other<br>Informations<br>can be displayed</p>

<footer class="site-footer abs">
<p style="top:31px">Home | About Us | Building | Construction Management | Project Management | Links | Free Downloads | Careers | Contacts</p>
<p style="top:55px">Copyright © 2008 Harlowe Bexley, All Rights Reserved - Webmaster &nbsp;&nbsp;&nbsp; | &nbsp;&nbsp;&nbsp; Privacy policy &nbsp;&nbsp;&nbsp; | &nbsp;&nbsp;&nbsp; Admin</p>
</footer>
</body>
</html>
```